Bright Path Estate Sales web design

We are looking to launch an Estate Sales Website for Nashville, TN. The name of our Business is Bright Path Estate Sales. We would like to give you a blank slate so that you can showcase your design skills for us. The few things we are looking for are a nice header graphic of a house or a stock image of an estate sale. Near the header graphic we would like a quick inquiry form. If not on the right side of the header maybe midway down the site. We potentially want to see what purple and Gold look like on the site however this is not a must. We have over 20 years of industry related experience.

1. Buttons at top of the website will be.
a. Services
b. Upcoming Sales
c. About Us
d. FAQs
e. Resources

Services we offer:
1. Estate Sales
2. Cleanouts
3. Appraisals

Sites We like:
https://www.kelvorintagsales.example/

We don't have a logo yet so if you have ideas please share them with us. Below are 2 ideas however if you have your own thoughts please ignore.

1. Oval ornate frame, gold and black, with BPES in the middle, deep purple. Think of catering to high class people..font should be fancy as opposed to simple.

2. Another option, Bright Path in bold fancy script, same colors, with Estate Sales below, small different font, black.

```html
<!DOCTYPE html>
<html lang="en">
<head>
<meta charset="utf-8">
<title>Bright Path Estate Sales</title>
<link rel="stylesheet" href="https://fonts.googleapis.com/css2?family=Libre+Baskerville:wght@400;700&family=Poppins:wght@400;500;600&display=swap">
<style>
:root{
  --purple:#5c2d91;
  --purple-dark:#4a2178;
  --gold:#f4c21a;
  --ink:#1b1b1f;
  --muted:#4d4d55;
  --hero-bg:#f8f6fb;
  --band-bg:#f4f2f7;
  --card-bg:#f7f5fa;
  --form-bg:#efe9f3;
  --footer-bg:#f2f0f5;
  --line:#d9d4e0;
  --white:#ffffff;
}
*{box-sizing:border-box;margin:0;padding:0}
html,body{width:1200px;height:3665px;overflow:hidden}
body{font-family:'Poppins',sans-serif;color:var(--ink);background:var(--white);position:relative}
.serif{font-family:'Libre Baskerville',serif}
.abs{position:absolute}
.btn{position:absolute;background:var(--purple);color:var(--white);font:500 13px 'Poppins',sans-serif;border-radius:5px;display:flex;align-items:center;justify-content:center}
.accent{color:var(--purple)}
.mark{position:absolute;width:14px;height:14px;background:var(--gold);border-radius:3px}

/* header */
.site-header{position:absolute;top:0;left:0;width:1200px;height:70px;background:var(--white)}
.brand{position:absolute;left:142px;top:22px;display:flex;align-items:center;gap:10px;font:700 20px 'Libre Baskerville',serif;color:var(--purple)}
.brand .sq{width:18px;height:18px;background:var(--gold)}
.nav{position:absolute;left:514px;top:26px;display:flex;gap:26px;font:500 13px 'Poppins',sans-serif}
.nav .first{font-weight:600}

/* hero */
.hero{position:absolute;top:70px;left:0;width:1200px;height:488px;background:var(--hero-bg)}
.hero h1{position:absolute;left:141px;top:150px;font:700 60px/1 'Libre Baskerville',serif;color:var(--purple)}
.hero h2{position:absolute;left:141px;top:228px;font:700 43px/1 'Libre Baskerville',serif;color:var(--ink)}
.hero p{position:absolute;left:141px;top:298px;font:500 16px 'Poppins',sans-serif}
.hero-photo{position:absolute;left:560px;top:80px;width:628px;height:345px;border-radius:6px;background:linear-gradient(160deg,#c9b89a 0%,#8a5a3c 45%,#5d5a57 75%,#9cae6a 100%)}

/* section heads */
.sec-title{position:absolute;left:0;width:1200px;text-align:center;font:700 29px 'Libre Baskerville',serif}

/* services */
.svc{position:absolute;top:773px;width:292px;height:240px;background:var(--card-bg);border-radius:16px;text-align:center}
.svc svg{margin-top:20px}
.svc h3{font:700 16px 'Libre Baskerville',serif;margin-top:10px}
.svc p{font:400 11.5px/20px 'Poppins',sans-serif;color:var(--muted);margin:12px 26px 0}
.svc a{display:inline-block;margin-top:12px;font:600 13px 'Poppins',sans-serif;color:var(--purple);text-decoration:underline}

/* about */
.about-arch{position:absolute;left:245px;top:1107px;width:230px;height:370px;border-radius:115px 115px 115px 115px;background:linear-gradient(170deg,#3b3a3a,#7a5a45 55,#d8c3a8);background:linear-gradient(170deg,#3b3a3a 0%,#7a5a45 55%,#d8c3a8 100%)}
.about-ring{position:absolute;left:262px;top:1100px;width:214px;height:380px;border:2px solid var(--purple);border-radius:107px;border-left-color:transparent}
.photo-card{position:absolute;background:var(--white);border-radius:8px;box-shadow:0 6px 20px rgba(0,0,0,.14);padding:6px}
.photo-card div{width:100%;height:100%;border-radius:6px}
.badge{position:absolute;left:427px;top:1330px;width:142px;height:104px;background:var(--white);border-radius:10px;box-shadow:0 6px 20px rgba(0,0,0,.12)}
.badge .num{position:absolute;left:68px;top:14px;font:700 42px/1 'Libre Baskerville',serif;color:var(--purple)}
.badge .lbl{position:absolute;left:10px;top:70px;font:600 13px 'Poppins',sans-serif}
.about-text h2{position:absolute;left:644px;top:1150px;font:700 29px 'Libre Baskerville',serif}
.about-text p{position:absolute;left:644px;width:415px;font:400 12.5px/22.5px 'Poppins',sans-serif;color:var(--muted)}

/* sales */
.sales{position:absolute;top:1569px;left:0;width:1200px;height:609px;background:var(--band-bg)}
.sale{position:absolute;top:178px;width:292px}
.sale .pic{height:222px}
.sale h4{margin-top:22px;font:600 15px 'Poppins',sans-serif;display:flex;justify-content:space-between;align-items:center}
.sale .loc{margin-top:10px;font:400 12.5px 'Poppins',sans-serif;color:var(--muted);display:flex;align-items:center;gap:8px}
.sale .date{margin-top:14px;font:500 12.5px 'Poppins',sans-serif}

/* testimonials */
.review{position:absolute;top:2434px;width:292px;height:228px;background:var(--white);border-radius:14px;box-shadow:0 4px 24px rgba(60,30,90,.08);text-align:center}
.review p{margin:70px 22px 0;font:500 11.5px/20.5px 'Poppins',sans-serif;height:74px}
.review .stars{margin-top:14px;color:#f59b2b;font-size:17px;letter-spacing:3px}
.review .who{margin-top:6px;font:600 15px 'Poppins',sans-serif}
.avatar{position:absolute;top:2398px;width:70px;height:70px;border-radius:50%;border:3px solid var(--white)}

/* form */
.inquiry{position:absolute;left:141px;top:2793px;width:918px;height:413px;background:var(--form-bg);border-radius:22px}
.inquiry .eyebrow{position:absolute;left:35px;top:43px;font:500 13px 'Poppins',sans-serif;color:var(--muted)}
.inquiry h3{position:absolute;left:35px;top:68px;font:600 17px 'Poppins',sans-serif}
.inquiry .rule{position:absolute;left:35px;top:99px;width:72px;height:2px;background:var(--purple)}
.field{position:absolute;background:var(--white);border:1px solid #e3dcea;border-radius:5px;font:400 11px 'Poppins',sans-serif;color:#8c8794;padding:12px 14px}
.form-photo{position:absolute;left:478px;top:58px;width:530px;height:300px;border-radius:6px;background:linear-gradient(160deg,#c9b89a 0%,#8a5a3c 45%,#5d5a57 75%,#9cae6a 100%)}

/* footer */
.site-footer{position:absolute;top:3291px;left:0;width:1200px;height:374px;background:var(--footer-bg)}
.foot-brand{position:absolute;left:141px;top:190px;font:700 38px/1 'Libre Baskerville',serif;color:var(--purple)}
.foot-brand-sq{position:absolute;left:195px;top:85px;width:80px;height:80px;background:var(--gold);border-radius:6px}
.foot-col{position:absolute;top:55px}
.foot-col h5{font:400 18px 'Libre Baskerville',serif;color:var(--purple);margin-bottom:18px}
.foot-col li{list-style:none;font:500 12.5px 'Poppins',sans-serif;margin-bottom:13px}
.contact li{display:flex;gap:10px;align-items:flex-start;line-height:18px}
.foot-rule{position:absolute;left:141px;top:320px;width:918px;height:1px;background:var(--line)}
.copy{position:absolute;left:141px;top:340px;font:500 12px 'Poppins',sans-serif}
.social{position:absolute;top:336px;width:24px;height:24px;border-radius:50%;background:var(--purple)}
</style>
</head>
<body>

<header class="site-header">
  <div class="brand"><span class="sq"></span>Bright Path</div>
  <nav class="nav"><span class="first">Home</span><span>About Us</span><span>Services</span><span>Sales</span><span>FAQ's</span><span>Resources</span></nav>
  <div class="btn" style="left:950px;top:17px;width:109px;height:35px">Contact Us</div>
</header>

<section class="hero">
  <span class="mark" style="left:143px;top:110px;width:20px;height:20px"></span>
  <h1>Bright Path</h1>
  <h2>Estate Sales</h2>
  <p>Nashville's Premier Estate Sale Company.</p>
  <div class="btn" style="left:141px;top:347px;width:110px;height:34px">Learn More</div>
  <div class="hero-photo" role="img" aria-label="Modern two-storey house with wood cladding, glass balconies and trees"></div>
</section>

<!-- services -->
<span class="mark" style="left:593px;top:660px"></span>
<h2 class="sec-title" style="top:694px">Our <span class="accent">Services</span></h2>

<div class="svc" style="left:141px">
  <svg width="76" height="72" viewBox="0 0 76 72" fill="none" stroke="var(--purple)" stroke-width="2.2" stroke-linecap="round" stroke-linejoin="round"><path d="M10 30 L38 6 L66 30"/><path d="M18 24 V44 M58 24 V44"/><circle cx="38" cy="26" r="7"/><path d="M38 33 V46"/><path d="M4 52 h14 c6 0 10 4 18 4 h14 c4 0 4 6 0 6 H30 M18 66 l30 0 c6 0 14-8 22-14"/></svg>
  <h3>Estate Sales</h3>
  <p>Lorem Ipsum is simply dummy text of the printing and typesetting industry.</p>
  <a>Read More &rarr;</a>
</div>
<div class="svc" style="left:454px">
  <svg width="76" height="72" viewBox="0 0 76 72" fill="none" stroke="var(--purple)" stroke-width="2.2" stroke-linecap="round" stroke-linejoin="round"><path d="M14 38 h10 v28 h-10 z"/><path d="M24 40 l10-14 c2-4 8-3 7 3 l-2 9 h14 c4 0 5 4 3 6 c3 2 2 6-1 7 c2 2 1 6-2 7 c1 3-1 6-4 6 H24"/><path d="M56 6 l2 6 6 2-6 2-2 6-2-6-6-2 6-2z"/><path d="M22 14 l1 4 4 1-4 1-1 4-1-4-4-1 4-1z"/><path d="M66 30 l1 3 3 1-3 1-1 3-1-3-3-1 3-1z"/></svg>
  <h3>Cleanouts</h3>
  <p>Lorem Ipsum is simply dummy text of the printing and typesetting industry.</p>
  <a>Read More &rarr;</a>
</div>
<div class="svc" style="left:767px">
  <svg width="76" height="72" viewBox="0 0 76 72" fill="none" stroke="var(--purple)" stroke-width="2.2" stroke-linecap="round" stroke-linejoin="round"><rect x="14" y="8" width="48" height="60" rx="4"/><rect x="28" y="4" width="20" height="8" rx="2"/><path d="M22 26 l3 3 5-5 M36 27 h18 M22 40 l3 3 5-5 M36 41 h18 M22 54 l3 3 5-5 M36 55 h18"/></svg>
  <h3>Appraisals</h3>
  <p>Lorem Ipsum is simply dummy text of the printing and typesetting industry.</p>
  <a>Read More &rarr;</a>
</div>

<!-- about -->
<div class="about-ring"></div>
<div class="about-arch" role="img" aria-label="Hands passing house keys across a desk with paperwork"></div>
<div class="photo-card" style="left:210px;top:1098px;width:82px;height:92px"><div role="img" aria-label="Small model house with a key" style="background:linear-gradient(150deg,#d9cfc4,#a33a35 60%,#7b6f66)"></div></div>
<div class="photo-card" style="left:141px;top:1302px;width:136px;height:158px"><div role="img" aria-label="White modern villa beside a pool" style="background:linear-gradient(170deg,#8fb3d9,#e8ecef 50%,#3aa6c4 85%)"></div></div>
<div class="badge">
  <svg class="abs" style="left:10px;top:16px" width="50" height="48" viewBox="0 0 50 48" fill="none" stroke="var(--purple)" stroke-width="2"><circle cx="25" cy="26" r="10"/><circle cx="25" cy="26" r="5"/><path d="M18 34 l-4 12 6-3 3 5 2-8 M32 34 l4 12-6-3-3 5-2-8"/><path d="M25 4 l1.5 3 3 .5-2 2 .5 3-3-1.5-3 1.5.5-3-2-2 3-.5z M8 12 l1 2 2 .3-1.5 1.4.4 2-1.9-1-1.9 1 .4-2L5 14.3l2-.3z M42 12 l1 2 2 .3-1.5 1.4.4 2-1.9-1-1.9 1 .4-2L39 14.3l2-.3z"/></svg>
  <div class="num">20</div>
  <div class="lbl">Years Experience</div>
</div>

<div class="about-text">
  <span class="mark" style="left:645px;top:1112px"></span>
  <h2>About <span class="accent">Bright Path</span></h2>
  <p style="top:1208px">It is a long established fact that a reader will be distracted by the readable content of a page when looking at its layout. The point of using Lorem Ipsum is that it has a more-or-less normal distribution of letters, as opposed to using 'Content here, content here', making it look like readable English.</p>
  <p style="top:1334px">There are many variations of passages of Lorem Ipsum available, but the majority have suffered alteration in some form, by injected humour, or randomised words which don't look even slightly believable.</p>
  <div class="btn" style="left:644px;top:1449px;width:110px;height:34px">Learn More</div>
</div>

<!-- upcoming sales -->
<section class="sales">
  <span class="mark" style="left:593px;top:63px"></span>
  <h2 class="sec-title" style="top:100px">Upcoming <span class="accent">Sales</span></h2>

  <div class="sale" style="left:141px">
    <div class="pic" role="img" aria-label="Two-storey suburban home with lit garage at dusk" style="background:linear-gradient(175deg,#6f8fb3 0%,#4d5a72 45%,#c89a62 70%,#9a9a98 100%)"></div>
    <h4>Phoenix Reserve Estate Sale <svg width="16" height="14" viewBox="0 0 16 14"><path d="M8 13 L1.5 6.5 A3.6 3.6 0 0 1 8 2.5 A3.6 3.6 0 0 1 14.5 6.5 Z" fill="var(--gold)"/></svg></h4>
    <div class="loc"><svg width="11" height="15" viewBox="0 0 11 15"><path d="M5.5 0 A5.5 5.5 0 0 1 11 5.5 C11 9 5.5 15 5.5 15 S0 9 0 5.5 A5.5 5.5 0 0 1 5.5 0Z" fill="var(--purple)"/><circle cx="5.5" cy="5.5" r="2" fill="#fff"/></svg>Houston, Texas</div>
    <div class="date">February 8–11</div>
  </div>
  <div class="sale" style="left:454px">
    <div class="pic" role="img" aria-label="Row of grey suburban houses with green lawns" style="background:linear-gradient(180deg,#8fc0ea 0%,#b9cfe0 40%,#7f7a78 62%,#5d8a3a 100%)"></div>
    <h4>Hacienda Estate Sale <svg width="16" height="14" viewBox="0 0 16 14"><path d="M8 13 L1.5 6.5 A3.6 3.6 0 0 1 8 2.5 A3.6 3.6 0 0 1 14.5 6.5 Z" fill="var(--gold)"/></svg></h4>
    <div class="loc"><svg width="11" height="15" viewBox="0 0 11 15"><path d="M5.5 0 A5.5 5.5 0 0 1 11 5.5 C11 9 5.5 15 5.5 15 S0 9 0 5.5 A5.5 5.5 0 0 1 5.5 0Z" fill="var(--purple)"/><circle cx="5.5" cy="5.5" r="2" fill="#fff"/></svg>Ft Worth, Texas</div>
    <div class="date">February 9–11</div>
  </div>
  <div class="sale" style="left:767px">
    <div class="pic" role="img" aria-label="Modern beige villa with glass walls and pool" style="background:linear-gradient(180deg,#a9c3dd 0%,#d8cdb8 40%,#c8a06a 70%,#b7c7cf 100%)"></div>
    <h4>Sonoran Villa Estate Sale <svg width="16" height="14" viewBox="0 0 16 14"><path d="M8 13 L1.5 6.5 A3.6 3.6 0 0 1 8 2.5 A3.6 3.6 0 0 1 14.5 6.5 Z" fill="var(--gold)"/></svg></h4>
    <div class="loc"><svg width="11" height="15" viewBox="0 0 11 15"><path d="M5.5 0 A5.5 5.5 0 0 1 11 5.5 C11 9 5.5 15 5.5 15 S0 9 0 5.5 A5.5 5.5 0 0 1 5.5 0Z" fill="var(--purple)"/><circle cx="5.5" cy="5.5" r="2" fill="#fff"/></svg>San Antonio, Texas</div>
    <div class="date">February 9–11</div>
  </div>

  <div class="btn" style="left:541px;top:532px;width:118px;height:34px">Registration</div>
</section>

<!-- testimonials -->
<span class="mark" style="left:593px;top:2275px"></span>
<h2 class="sec-title" style="top:2313px">What Our <span class="accent">Clients</span> Say</h2>

<div class="review" style="left:141px"><p>It is a long established fact that a reader will be distracted by the readable content of a page when looking at its layout.</p><div class="stars">★★★★★</div><div class="who">Maren T.</div></div>
<div class="review" style="left:454px"><p>There are many variations of passages of Lorem Ipsum available, but the majority have suffered alteration in some form.</p><div class="stars">★★★★★</div><div class="who">Rosa K.</div></div>
<div class="review" style="left:767px"><p>Lorem Ipsum is simply dummy text of the printing and typesetting industry.</p><div class="stars">★★★★★</div><div class="who">Devin L.</div></div>
<div class="avatar" style="left:252px;background:#b8413f" role="img" aria-label="Client portrait"></div>
<div class="avatar" style="left:565px;background:#4f6b5f" role="img" aria-label="Client portrait"></div>
<div class="avatar" style="left:878px;background:#3e3a3c" role="img" aria-label="Client portrait"></div>

<svg class="abs" style="left:560px;top:2693px" width="80" height="16" viewBox="0 0 80 16" fill="none" stroke="var(--purple)" stroke-width="1.8" stroke-linecap="round"><path d="M26 8 H2 M8 2 L2 8 L8 14"/><path d="M54 8 H78 M72 2 L78 8 L72 14"/></svg>

<!-- inquiry form -->
<section class="inquiry">
  <div class="eyebrow">Request More Information About</div>
  <h3>Bright Path Estate Sales</h3>
  <div class="rule"></div>
  <div class="field" style="left:35px;top:113px;width:200px;height:38px">Name*</div>
  <div class="field" style="left:248px;top:113px;width:200px;height:38px">Email*</div>
  <div class="field" style="left:35px;top:166px;width:413px;height:38px">Phone*</div>
  <div class="field" style="left:35px;top:219px;width:413px;height:106px">Message</div>
  <div class="btn" style="left:35px;top:346px;width:110px;height:34px">Submit</div>
  <div class="form-photo" role="img" aria-label="Modern two-storey house with wood cladding and landscaped garden"></div>
</section>

<!-- footer -->
<footer class="site-footer">
  <div class="foot-brand-sq"></div>
  <div class="foot-brand">Bright Path</div>
  <div class="foot-col" style="left:423px"><h5>Quick Links</h5><ul><li>Home</li><li>About Us</li><li>Services</li><li>Sales</li><li>FAQ's</li><li>Resources</li></ul></div>
  <div class="foot-col" style="left:637px"><h5>Company</h5><ul><li>Terms &amp; Condition</li><li>Privacy Policy</li><li>Contact Us</li></ul></div>
  <div class="foot-col contact" style="left:848px"><h5>Contact Info</h5><ul>
    <li><svg width="16" height="18" viewBox="0 0 16 18" fill="none" stroke="var(--purple)" stroke-width="1.6"><path d="M8 1 A5 5 0 0 1 13 6 C13 9 8 14 8 14 S3 9 3 6 A5 5 0 0 1 8 1Z"/><circle cx="8" cy="6" r="1.8"/><path d="M3 13 C-1 15 17 17 13 13"/></svg><span>Address Line 1, Address Line<br>2, Address Line 3.</span></li>
    <li><svg width="16" height="14" viewBox="0 0 16 14"><rect x="0" y="1" width="16" height="12" rx="2" fill="var(--purple)"/><path d="M1 3 L8 8 L15 3" stroke="#fff" stroke-width="1.4" fill="none"/></svg><span>info@brightpath.example</span></li>
    <li><svg width="16" height="16" viewBox="0 0 16 16"><path d="M3 1 L6 1 L7 5 L5 6.5 C6 9 7.5 10.5 9.5 11 L11 9 L15 10 L15 13 C15 14 14 15 13 15 C6 14 2 10 1 3 C1 2 2 1 3 1Z" fill="var(--purple)"/></svg><span>615-555-0142</span></li>
  </ul></div>
  <div class="foot-rule"></div>
  <div class="copy">© 2024 Bright Path Estate Sales. All Rights Reserved.</div>
  <span class="social" style="left:926px"></span>
  <span class="social" style="left:962px"></span>
  <span class="social" style="left:998px"></span>
  <span class="social" style="left:1034px"></span>
</footer>

</body>
</html>
```